Construction Company

I'm a new construction company called Tembrik Construction. I want my card to look simple and clean. I have provided a sample of what I want the front to look like (Tembrik_Card.jpeg) and a back ground for the back of the (Tembrik_Card_Background.jpeg) - the background can be faded so my name and other information is more prominent.
Construction

```html
<!DOCTYPE html>
<html lang="en">
<head>
<meta charset="utf-8">
<title>Tembrik Construction – Business Card</title>
<link href="https://fonts.googleapis.com/css2?family=Josefin+Sans:wght@400&family=Open+Sans:wght@400;600&display=swap" rel="stylesheet">
<style>
  :root {
    --backdrop: #e8e3da;
    --card-white: #ffffff;
    --card-shade: #eeeeee;
    --brand-orange: #f7a11a;
    --brand-dark: #3b3626;
    --ink: #3a3a3a;
    --plan-tone: #e4e4e4;
  }
  html, body {
    margin: 0;
    padding: 0;
    width: 1200px;
    height: 1200px;
    overflow: hidden;
    background: var(--backdrop);
  }
  .canvas {
    position: relative;
    width: 1200px;
    height: 1200px;
  }
  .card {
    position: absolute;
    left: 170px;
    width: 860px;
    height: 500px;
    box-shadow: 0 6px 14px rgba(0,0,0,0.25);
    overflow: hidden;
  }
  /* Front */
  .card-front {
    top: 45px;
    background: linear-gradient(160deg, var(--card-white) 35%, var(--card-shade) 100%);
  }
  .plan-area {
    position: absolute;
    left: 128px;
    top: 33px;
    width: 607px;
    height: 435px;
    background: radial-gradient(ellipse at center, var(--plan-tone) 0%, rgba(228,228,228,0.35) 70%, rgba(228,228,228,0) 100%);
    opacity: 0.7;
  }
  .stripe {
    position: absolute;
    top: 0;
    height: 100%;
  }
  .stripe-dark { left: 772px; width: 9px; background: var(--brand-dark); }
  .stripe-orange { left: 795px; width: 11px; background: var(--brand-orange); }
  .identity {
    position: absolute;
    right: 177px;
    top: 104px;
    text-align: right;
  }
  .person-name {
    margin: 0;
    font-family: "Josefin Sans", sans-serif;
    font-weight: 400;
    font-size: 40px;
    letter-spacing: 1px;
    text-transform: uppercase;
    color: var(--brand-orange);
    line-height: 1;
  }
  .person-role {
    margin: 4px 0 0;
    font-family: "Open Sans", sans-serif;
    font-size: 21px;
    color: var(--ink);
  }
  .contact {
    position: absolute;
    left: 75px;
    top: 338px;
    font-family: "Open Sans", sans-serif;
    font-size: 22px;
    line-height: 33px;
    color: var(--ink);
  }
  .contact p { margin: 0; }
  .contact .label {
    color: var(--brand-orange);
    font-weight: 600;
  }
  /* Back */
  .card-back {
    top: 650px;
    background: var(--brand-dark);
  }
  .brand-lockup {
    position: absolute;
    left: 0;
    right: 0;
    top: 170px;
    text-align: center;
    color: var(--brand-orange);
    font-family: "Josefin Sans", sans-serif;
    font-weight: 400;
  }
  .brand-name {
    margin: 0;
    font-size: 100px;
    line-height: 1;
    letter-spacing: 4px;
    text-transform: uppercase;
  }
  .brand-line {
    margin: 16px 0 0;
    font-size: 23px;
    letter-spacing: 14px;
    padding-left: 14px;
    text-transform: uppercase;
  }
</style>
</head>
<body>
<main class="canvas">
  <section class="card card-front">
    <div class="plan-area" role="img" aria-label="Faint architectural floor plan background"></div>
    <div class="stripe stripe-dark"></div>
    <div class="stripe stripe-orange"></div>
    <div class="identity">
      <h1 class="person-name">Marek Tembrik</h1>
      <p class="person-role">Manager</p>
    </div>
    <address class="contact" style="font-style: normal;">
      <p>4820 Holloway Ave Suite 212</p>
      <p><span class="label">tel:</span> 555.214.7730 <span class="label">fax:</span> 555.214.7731</p>
      <p><span class="label">email:</span> m.tembrik@tembrikbuild.com</p>
    </address>
  </section>

  <section class="card card-back">
    <div class="brand-lockup">
      <p class="brand-name">Tembrik</p>
      <p class="brand-line">Construction</p>
    </div>
  </section>
</main>
</body>
</html>
```